Packaging design for an cardboard box / carton for modern Scandinavian cushion covers

The design should be made on a finished pattern for a cardboard box / carton. Ideally, the design can be directly on a packaging manufacturer. The box should measure 250 x 180 x 50 mm. Skanidnavian packaging design for modern cushion covers with classic patterns. The color design of the packaging should be kept simple and not too overloaded. 10 euros on a cushion cover.

Target Market(s)

End customer / retail

Requirements
Must have
• The logo (see appendix) should be included as well as a cut-out through which the customer can see the pattern of the product.
Nice to have
• Please attach the German texts (see appendix) to the draft.

```html
<!DOCTYPE html>
<html lang="de">
<head>
<meta charset="utf-8">
<title>Kissenbezug Faltschachtel – Entwürfe</title>
<link rel="stylesheet" href="https://fonts.googleapis.com/css2?family=PT+Sans:wght@400;700&display=swap">
<style>
  :root {
    --blue: #22a6c8;
    --graphite: #58585a;
    --paper: #ffffff;
    --ink: #4d4d4f;
    --cutline: #9a9a9a;
    --pattern-light: #d4d4d4;
    --pattern-dark: #9e9e9e;
  }
  html, body {
    margin: 0;
    padding: 0;
    width: 820px;
    height: 1200px;
    overflow: hidden;
    background: var(--paper);
  }
  .dieline-sheet {
    display: block;
    width: 820px;
    height: 1200px;
    font-family: "PT Sans", sans-serif;
  }
  .flap { fill: var(--paper); stroke: var(--cutline); stroke-width: 0.6; }
  .fold { fill: none; stroke: var(--cutline); stroke-width: 0.5; }
  .fill-blue { fill: var(--blue); }
  .fill-graphite { fill: var(--graphite); }
  .fill-paper { fill: var(--paper); }
  .swoosh-light { fill: none; stroke: var(--paper); stroke-width: 0.9; }
  .swoosh-blue { fill: none; stroke: var(--blue); stroke-width: 0.9; }
  .swoosh-dark { fill: none; stroke: var(--graphite); stroke-width: 0.9; }
  .body-copy { font-size: 6.4px; fill: var(--ink); }
  .body-copy.on-dark { fill: var(--paper); }
  .product-title { font-size: 8.6px; font-weight: 700; fill: var(--ink); text-anchor: end; }
  .product-title.on-dark { fill: var(--paper); }
  .product-spec { font-size: 6.4px; fill: var(--ink); text-anchor: end; }
  .product-spec.on-dark { fill: var(--paper); }
  .side-url { font-size: 14px; fill: var(--ink); text-anchor: middle; }
  .side-url.muted { fill: #6d6d70; }
  .brand-name { font-size: 6px; font-weight: 700; fill: var(--ink); }
  .brand-name.on-dark { fill: var(--paper); }
  .brand-dot { fill: var(--blue); }
  .brand-dot.on-blue { fill: var(--paper); }
  .pattern-window { fill: url(#patternTone); }
</style>
</head>
<body>
<svg class="dieline-sheet" viewBox="0 0 690 1010" preserveAspectRatio="xMidYMid meet" xmlns="http://www.w3.org/2000/svg">
  <defs>
    <linearGradient id="patternTone" x1="0" y1="0" x2="1" y2="1">
      <stop offset="0" stop-color="var(--pattern-light)"/>
      <stop offset="0.5" stop-color="var(--pattern-dark)"/>
      <stop offset="1" stop-color="var(--pattern-light)"/>
    </linearGradient>
  </defs>

  <!-- ============ Variante 1: weiss mit blauen Bögen ============ -->
  <g class="carton carton-light">
    <g class="flaps">
      <polygon class="flap" points="48,93 52,42 60,30 262,30 268,42 272,93"/>
      <polygon class="flap" points="272,93 274,50 284,32 326,32 333,50 335,93"/>
      <polygon class="flap" points="335,93 339,42 347,30 549,30 555,42 557,93"/>
      <polygon class="flap" points="557,93 559,50 568,32 608,32 615,50 617,93"/>
      <polygon class="flap" points="48,403 52,454 60,465 262,465 268,454 272,403"/>
      <polygon class="flap" points="272,403 274,446 284,463 326,463 333,446 335,403"/>
      <polygon class="flap" points="335,403 339,454 347,465 549,465 555,454 557,403"/>
      <polygon class="flap" points="557,403 559,446 568,463 608,463 615,446 617,403"/>
    </g>
    <rect class="fill-paper" x="48" y="93" width="569" height="310"/>

    <g class="panel back-panel">
      <path class="fill-blue" d="M48,93 L98,93 C110,255 180,365 272,403 L48,403 Z"/>
      <path class="swoosh-light" d="M68,93 C82,262 165,372 272,403"/>
      <path class="swoosh-light" d="M76,93 C90,260 170,370 272,403"/>
      <path class="swoosh-light" d="M86,93 C99,258 175,368 272,403"/>
      <g class="body-copy">
        <text x="145" y="158" textLength="103" lengthAdjust="spacing">Mit diesem Kissenbezug erwerben</text>
        <text x="145" y="170" textLength="103" lengthAdjust="spacing">Sie nicht nur einen Hingucker der</text>
        <text x="145" y="182" textLength="103" lengthAdjust="spacing">Ihrem Sofa den letzten Hauch</text>
        <text x="145" y="194" textLength="103" lengthAdjust="spacing">Gemütlichkeit und Stil verpasst,</text>
        <text x="145" y="206" textLength="103" lengthAdjust="spacing">sondern entscheiden sich auch für</text>
        <text x="145" y="218">100% Qualität und Langlebigkeit.</text>
        <text x="145" y="240" textLength="103" lengthAdjust="spacing">Unsere Kissenebzüge bestehen aus</text>
        <text x="145" y="252" textLength="103" lengthAdjust="spacing">100% Leinen bzw. Baumwolle und</text>
        <text x="145" y="264" textLength="103" lengthAdjust="spacing">wurden von unseren ausgewählten</text>
        <text x="145" y="276">Partnern nachhaltig hergestellt.</text>
      </g>
      <g class="brand-mark">
        <circle class="brand-dot" cx="196" cy="354" r="5"/>
        <text class="brand-name" x="204" y="356.5">mein-kissenhaus.de</text>
      </g>
    </g>

    <g class="panel side-panel">
      <path class="fill-blue" d="M272,403 C296,330 316,220 326,93 C331,210 334,310 335,403 Z"/>
      <text class="side-url" transform="translate(298 220) rotate(-90)">mein-kissenhaus.de</text>
    </g>

    <g class="panel front-panel">
      <path class="fill-blue" d="M335,93 L372,93 C382,255 455,372 557,396 L557,403 L335,403 Z"/>
      <path class="swoosh-light" d="M350,93 C362,265 440,380 557,403"/>
      <path class="swoosh-light" d="M358,93 C370,262 446,378 557,401"/>
      <path class="swoosh-light" d="M365,93 C376,258 450,375 557,399"/>
      <path class="pattern-window" role="img" aria-label="Sichtfenster mit grau-weissem Kissenbezugmuster" d="M374,146 L518,146 Q530,146 530,158 L530,272 L374,272 Z"/>
      <text class="product-title" x="548" y="291">Gemütlichkeit im</text>
      <text class="product-title" x="548" y="302">Skandinavischen Stil</text>
      <text class="product-spec" x="548" y="315">45 x 45 cm | 100 % Leinen</text>
      <text class="product-spec" x="548" y="325">Mit Reissverschluss</text>
      <g class="brand-mark">
        <circle class="brand-dot" cx="479" cy="354" r="5"/>
        <text class="brand-name" x="487" y="356.5">mein-kissenhaus.de</text>
      </g>
    </g>

    <g class="panel side-panel">
      <path class="fill-blue" d="M609,93 L617,93 L617,403 L561,403 C588,330 604,230 609,93 Z"/>
      <path class="swoosh-light" d="M613,93 C609,240 590,340 566,403"/>
    </g>

    <g class="folds">
      <rect class="fold" x="48" y="93" width="569" height="310"/>
      <line class="fold" x1="272" y1="93" x2="272" y2="403"/>
      <line class="fold" x1="335" y1="93" x2="335" y2="403"/>
      <line class="fold" x1="557" y1="93" x2="557" y2="403"/>
    </g>
  </g>

  <!-- ============ Variante 2: graphit mit blauen Bögen ============ -->
  <g class="carton carton-dark">
    <g class="flaps">
      <polygon class="flap" points="48,568 52,517 60,505 262,505 268,517 272,568"/>
      <polygon class="flap" points="272,568 274,525 284,507 326,507 333,525 335,568"/>
      <polygon class="flap" points="335,568 339,517 347,505 549,505 555,517 557,568"/>
      <polygon class="flap" points="557,568 559,525 568,507 608,507 615,525 617,568"/>
      <polygon class="flap" points="48,878 52,929 60,940 262,940 268,929 272,878"/>
      <polygon class="flap" points="272,878 274,921 284,938 326,938 333,921 335,878"/>
      <polygon class="flap" points="335,878 339,929 347,940 549,940 555,929 557,878"/>
      <polygon class="flap" points="557,878 559,921 568,938 608,938 615,921 617,878"/>
    </g>
    <rect class="fill-graphite" x="48" y="568" width="569" height="310"/>

    <g class="panel back-panel">
      <path class="fill-blue" d="M92,568 L272,568 L272,878 C170,845 104,730 92,568 Z"/>
      <path class="swoosh-blue" d="M80,568 C94,735 165,850 272,878"/>
      <path class="swoosh-blue" d="M72,568 C86,738 160,853 272,878"/>
      <path class="swoosh-dark" d="M100,568 C112,728 176,838 272,872"/>
      <g class="body-copy on-dark">
        <text x="145" y="633" textLength="103" lengthAdjust="spacing">Mit diesem Kissenbezug erwerben</text>
        <text x="145" y="645" textLength="103" lengthAdjust="spacing">Sie nicht nur einen Hingucker der</text>
        <text x="145" y="657" textLength="103" lengthAdjust="spacing">Ihrem Sofa den letzten Hauch</text>
        <text x="145" y="669" textLength="103" lengthAdjust="spacing">Gemütlichkeit und Stil verpasst,</text>
        <text x="145" y="681" textLength="103" lengthAdjust="spacing">sondern entscheiden sich auch für</text>
        <text x="145" y="693">100% Qualität und Langlebigkeit.</text>
        <text x="145" y="715" textLength="103" lengthAdjust="spacing">Unsere Kissenebzüge bestehen aus</text>
        <text x="145" y="727" textLength="103" lengthAdjust="spacing">100% Leinen bzw. Baumwolle und</text>
        <text x="145" y="739" textLength="103" lengthAdjust="spacing">wurden von unseren ausgewählten</text>
        <text x="145" y="751">Partnern nachhaltig hergestellt.</text>
      </g>
      <g class="brand-mark">
        <circle class="brand-dot" cx="74" cy="835" r="5"/>
        <text class="brand-name on-dark" x="82" y="837.5">mein-kissenhaus.de</text>
      </g>
    </g>

    <g class="panel side-panel">
      <path class="fill-blue" d="M272,568 L322,568 C318,720 300,820 272,878 Z"/>
      <path class="swoosh-dark" d="M327,568 C322,725 302,825 274,878"/>
      <text class="side-url" transform="translate(298 680) rotate(-90)">mein-kissenhaus.de</text>
    </g>

    <g class="panel front-panel">
      <path class="fill-blue" d="M374,568 L557,568 L557,878 C455,852 386,735 374,568 Z"/>
      <path class="swoosh-blue" d="M360,568 C372,740 445,858 557,878"/>
      <path class="swoosh-blue" d="M352,568 C364,743 440,862 557,878"/>
      <path class="swoosh-dark" d="M382,568 C394,730 460,840 557,872"/>
      <rect class="pattern-window" role="img" aria-label="Sichtfenster mit grau-weissem Kissenbezugmuster" x="388" y="596" width="140" height="122"/>
      <text class="product-title on-dark" x="527" y="771">Gemütlichkeit im</text>
      <text class="product-title on-dark" x="527" y="782">Skandinavischen Stil</text>
      <text class="product-spec on-dark" x="527" y="805">45 x 45 cm</text>
      <text class="product-spec on-dark" x="527" y="814">Mit Reissverschluss</text>
      <text class="product-spec on-dark" x="527" y="823">100 % Leinen</text>
      <g class="brand-mark">
        <circle class="brand-dot" cx="360" cy="835" r="5"/>
        <text class="brand-name on-dark" x="368" y="837.5">mein-kissenhaus.de</text>
      </g>
    </g>

    <g class="panel side-panel">
      <text class="side-url muted" transform="translate(583 690) rotate(-90)">mein-kissenhaus.de</text>
    </g>

    <g class="folds">
      <rect class="fold" x="48" y="568" width="569" height="310"/>
      <line class="fold" x1="272" y1="568" x2="272" y2="878"/>
      <line class="fold" x1="335" y1="568" x2="335" y2="878"/>
      <line class="fold" x1="557" y1="568" x2="557" y2="878"/>
    </g>
  </g>
</svg>
</body>
</html>
```